上記のような特長を持つ、弊店主力商品 「珪藻土コースター」を、定期販売する予定です。
主なターゲットは、飲食店さまです。

この珪藻土コースターは、吸水性とその高級感から、導入当初は喜ばれますが、しばらく使い続けていると、コースター表面上の目詰まりから、吸水性が悪くなることがわかってきました。

まとめて数十枚ご購入いただくと、飲食店様にとっては、そんなに安い買い物ではないと思っています。(弊店の売り上げにはなるので、もちろんうれしいのですが)

従いまして、コースターの吸水力が落ちてきたときに、そのコースターを新品と少しずつ交換できるようなプランがあれば、と思い珪藻土コースターの「毎月お届けコース」(定期購入プラン)を立ち上げることにいたしました。

つまりは、珪藻土コースターを導入された飲食店様に対して、定期的に数枚程度ご購入いただき、吸水性が悪くなったものを廃棄していただくことで、吸水力が高い状態を維持していただるようなプランをご提案したいと思っています。

つきまして、お願いしたいことは、この商品のサイト上の購入ページをデザインしていただけないか、ということでございます。
状況の説明等のテキスト文は、ある程度作りました。(添付:cst_monthly_story.txt)従いまして、添付したテキストを主に使っていただき、イラストや写真等を付加していただき、申し込みたくなるような商品購入ページ(毎月お届けプランを申し込みたくなるようなページ)をデザインしていただけないか、というお願いになります。

製作にあたりましての条件は下記になります
【諸条件について】
・添付したテキスト文をお使いいただき、レイアウトをお願いします。
・その他、ご自身で追加されたテキストを加えていただいても一向にかまいません。
・弊店サイトにある、テキストや写真は、如何様にでもアレンジしたりして使っていただいて結構です。
・説明等のため、独自のイラストや、写真などを付加していただけるとありがたいですが、納品いただいたコンテンツは、弊店サイトや、場合によってはチラシ等で流用させていただくこともあるかもしれませんので、著作権(もしくは、弊店での使用権)はフルにいただける状況でのご提案をお願いします。
・当デザインいただくページは、その内容柄、流用の上、複数のページができる予定です。(1枚のコース、2枚のコース や、オリジナルコースターのページ、●●絵柄のページなどなど)また、当方にて、加工・加筆修正等もさせていただくことがあります。また、弊社にて各所に流用されることを予めご承知おきくださいませ。

【納品物について】
・イラストレーターで写真等をレイアウトいただいた場合は、貼り付けた元画像(元イラスト)のデータも併せて納品をお願いいたします。(psd形式でも、aiでも、jpegでも結構です)イラストデータの場合は、こちらで拡大縮小することも考えられますので、aiデータをお願いします。
・デザイン(&レイアウト)が依頼のメインですので、イラストレーターファイルのみでも結構ですが、HTMLファイルででも納品いただければ、うれしいです(必須ではありません)
※要は、イラストレーターファイル、html もしくはその両方の納品をお願いします。
・イラストレーターのファイルは、当方環境の関係上、cs4 以下での保存での納品をお願いします。

以上です。

ご説明不足もあるかもしれません。
ご質問等あれば、是非くださいませ。

【その他】
場合によっては、今後、継続的にお願いさせていただくかもしれません。
可能であれば、
・過去に作ったことのあるページデザイン(作品)のurl
(商品ページでなくとも、トップでもランディングページでもなんでも結構です)
・直接依頼させていただくときのご希望の単価
も一緒にいただけると嬉しいです。(もちろん、なくともかまいませんので)

商品価格(●●円で結構です)、添付のテキストの内容
A4
片面
シンプル 複雑
単色 カラフル
暗い 明るい
日常 高級
遊び心 厳粛
未来的 伝統的
女性的 男性的
何がいいのか、含めて、ご提案お願いします。
• 高解像度JPG (.jpg)
• イラストレーター形式 (.ai)
依頼金額を24000円に変更して、延長しました。
一度、締め切りを経過したのですが、
誠に申し訳ありません、恐縮ながら納得できるものがありませんでしたので、延長させていただきました。こちらの依頼内容も説明が長いばっかりで、的を得ておらず、広すぎて良くなかったと思います。申し訳ありませんでした。

改めまして依頼内容を改めさせていただき、本追記内容をご参照の上、再提案頂戴できれば嬉しいです。何卒、よろしくお願い致します。
http://www.morikane-do.com/SHOP/MKTB-QX-LNE07-03.html
(ID:rp、pw:pwd)
上記サイトをご覧頂き、
2箇所の画像箇所
・コースター毎月お届けコース1
・コースター毎月お届けコース2
の上記2箇所に入る、********************
※下の二箇所(コースターの写真、スケジュールサイクルの図 は ご提案不要です)
画像は、サイズを変更したりしますので、イラストレーターファイル(CS4以下)か、高解像度画像の納品をお願いします。

よろしくお願いします。
本依頼内容を、Webサイトのページ作成へ、カテゴリ変更させていただきます。それに伴い、増額させていただきました。
また、上記追記で、イラスト(等で、窓枠を埋める)2点の追加 をお願いしている形になっております。

もちろん、イラスト2点追加でもかまいませんし、それにとらわれなくとも結構です。本来は、「毎月購入コース」をご購入いただくためのページですので、それを喚起できるようであればどのようにデザインいただいてもかまいません。
(商品の仕様上の趣旨は変更できませんが。)

よろしくお願いいたします。

甲乙つけ難かったのですが、
弊店の弱点をうまく突いて(フォローして)いただけましたので、
決めました。

ご提案、誠にありがとうございました。
一つしか選べなくて心苦しいですが、
又の機会に、今後とも、よろしくお願いできれば幸いです。
ありがとうございました。

```html
<!DOCTYPE html>
<html lang="ja">
<head>
<meta charset="utf-8">
<title>森金堂 珪藻土コースター 毎月お届けコース</title>
<link href="https://fonts.googleapis.com/css2?family=Noto+Sans+JP:wght@400;700;900&family=Noto+Serif+JP:wght@600;900&display=swap" rel="stylesheet">
<style>
:root{
  --green:#7aa22c;
  --green-dark:#4f7a16;
  --green-light:#eef5dc;
  --blue:#2f7fc1;
  --blue-light:#e6f1fa;
  --orange:#e8741a;
  --red:#d9372b;
  --ink:#333;
  --muted:#777;
  --line:#d5d5d5;
  --panel:#f4f4f4;
}
*{box-sizing:border-box;margin:0;padding:0}
html,body{width:1200px;height:3256px;overflow:hidden}
body{font-family:"Noto Sans JP",sans-serif;color:var(--ink);background:#fff;font-size:14px;line-height:1.6;position:relative}
.site-header{height:68px;display:flex;align-items:center;padding:0 24px;border-bottom:1px solid var(--line)}
.brand{display:flex;align-items:center;gap:10px;font-size:30px;font-weight:700;color:var(--green-dark)}
.brand-mark{width:30px;height:30px;background:var(--green-dark)}
.brand-sub{font-size:12px;color:var(--muted);margin-left:16px}
.search{margin-left:auto;display:flex;gap:6px}
.search-field{width:210px;height:28px;border:1px solid var(--line)}
.search-btn{height:28px;padding:0 14px;background:#666;color:#fff;font-size:13px;line-height:28px}
.tel{margin-left:30px;background:var(--blue);color:#fff;border-radius:16px;padding:4px 20px;font-size:22px;font-weight:700}
.global-nav{height:30px;margin:8px 0;background:linear-gradient(#9cc34a,var(--green));display:flex}
.global-nav a{flex:1;text-align:center;color:#fff;font-size:13px;line-height:30px;border-right:1px solid rgba(255,255,255,.5);text-decoration:none}
.layout{display:flex;padding:0 10px}
.sidebar{width:205px;flex-shrink:0;font-size:12px}
.side-block{margin-bottom:18px}
.side-title{background:var(--panel);border-left:4px solid var(--green);padding:4px 8px;font-weight:700;margin-bottom:6px}
.side-list li{list-style:none;padding:3px 8px;border-bottom:1px dotted var(--line)}
.side-banner{height:160px;background:var(--blue);color:#fff;padding:14px;font-weight:700;font-size:20px;margin-bottom:14px}
.side-banner small{display:block;font-size:12px;font-weight:400;margin-top:6px}
.side-point{height:90px;border:2px solid var(--orange);color:var(--orange);text-align:center;padding-top:10px;font-size:30px;font-weight:900;margin-bottom:14px}
.side-point small{display:block;font-size:12px;font-weight:400;color:var(--ink)}
.side-affiliate{height:90px;background:var(--green-light);padding:12px;font-weight:700;color:var(--green-dark);font-size:18px;margin-bottom:18px}
.calendar{width:100%;border-collapse:collapse;font-size:11px}
.calendar td{border:1px solid var(--line);text-align:center;height:22px}
.calendar .closed{background:#f6d4d4}
.partner{height:40px;background:var(--panel);margin-bottom:6px}
.main{flex:1;padding-left:16px;min-width:0}
.breadcrumb{font-size:12px;color:var(--muted);margin:8px 0 12px}
.offers{display:flex;gap:16px;height:140px}
.offer{flex:1;border:1px solid var(--line);display:flex;align-items:center;padding:14px;gap:14px}
.offer p{font-size:15px;font-weight:700}
.offer em{font-style:normal;color:var(--red)}
.offer-btn{display:inline-block;margin-top:8px;background:var(--green);color:#fff;padding:4px 16px;font-size:12px;border-radius:3px}
.offer-photo{width:150px;height:100px;flex-shrink:0;background:linear-gradient(135deg,#e9e3d6,#cfc3ad)}
.order-note{text-align:center;color:var(--red);font-weight:700;font-size:18px;margin:12px 0}
.hero{height:360px;position:relative;background:linear-gradient(#f7f9f1,#e7ecd8);border:1px solid var(--line);overflow:hidden}
.hero-tag{position:absolute;left:20px;top:10px;font-size:20px;font-weight:900;color:var(--orange);line-height:28px}
.hero-course{position:absolute;left:20px;top:40px;background:var(--green);color:#fff;font-size:30px;font-weight:900;padding:0 18px;line-height:48px;z-index:2}
.hero-photo{position:absolute;left:0;top:100px;width:310px;height:260px;background:radial-gradient(circle at 50% 45%,#f3efe6,#b8c6a0)}
.hero-brand{position:absolute;right:20px;top:14px;font-weight:700;color:var(--green-dark);font-size:18px}
.hero-title{position:absolute;left:340px;top:78px;font-size:42px;font-weight:900;color:var(--green-dark);line-height:1.15}
.hero-title small{display:block;font-size:20px;color:var(--ink);line-height:1.4}
.hero-badges{position:absolute;left:340px;top:262px;display:flex;gap:6px}
.hero-badges span{width:62px;height:62px;border-radius:50%;background:var(--green);color:#fff;font-size:11px;display:flex;align-items:center;justify-content:center;text-align:center;font-weight:700;line-height:1.3}
.hero-price{position:absolute;right:24px;bottom:18px;font-size:56px;font-weight:900;color:var(--red);line-height:1}
.hero-price small{font-size:22px}
.feature{height:300px;position:relative;margin-top:20px;background:linear-gradient(90deg,#fff 40%,var(--blue-light));overflow:hidden}
.feature-head{position:absolute;left:20px;top:40px;font-family:"Noto Serif JP",serif;font-size:44px;font-weight:900;color:var(--blue)}
.feature-head small{font-size:30px;color:var(--ink)}
.feature-lead{position:absolute;left:20px;top:110px;font-family:"Noto Serif JP",serif;font-size:26px;font-weight:600}
.feature-photo{position:absolute;right:0;top:0;width:360px;height:300px;background:radial-gradient(circle,#d7efe9,#9cc7c0)}
.feature.second{background:linear-gradient(90deg,#fff 40%,var(--green-light))}
.feature.second .feature-head{color:var(--green)}
.feature.second .feature-photo{background:radial-gradient(circle,#e6f0d0,#9fbd72)}
.about-head{margin-top:24px;border-bottom:3px solid var(--green);padding:10px 0;font-size:22px;font-weight:700;color:var(--green-dark)}
.about-head span{font-size:12px;background:var(--orange);color:#fff;padding:2px 8px;margin-right:10px;vertical-align:middle}
.about-lead{margin-top:14px;border:2px solid var(--blue);padding:18px 22px;font-size:18px;font-weight:700;line-height:1.8}
.about-lead b{color:var(--blue)}
.about-body{display:flex;gap:20px;margin-top:20px;height:300px}
.about-text{flex:1;font-size:13px;line-height:2}
.about-img{width:180px;height:180px;flex-shrink:0;border-radius:50%;background:radial-gradient(#efe6d3,#c9b995)}
.about-img.pattern{border-radius:0;background:linear-gradient(135deg,#eaf2fa,#b9cfe6)}
.summary{border:2px dashed var(--green);background:var(--green-light);padding:16px 22px;font-size:14px;line-height:1.9;height:120px;margin-top:4px}
.summary b{color:var(--red)}
.product{margin-top:30px;border:2px solid var(--green);padding:16px 22px;height:100px}
.product h2{font-size:22px;color:var(--green-dark)}
.details{margin-top:20px;border:1px solid var(--line);padding:20px 26px;height:1040px;position:relative;font-size:13px;line-height:2}
.details h3{font-size:14px;color:var(--green-dark);margin-top:14px}
.icons{position:absolute;right:30px;top:20px;display:flex;gap:14px}
.icon-day{width:120px;height:120px;border-radius:50%;background:var(--orange);color:#fff;text-align:center;padding-top:22px;font-weight:900;font-size:34px;line-height:1.1}
.icon-day small{display:block;font-size:14px}
.icon-mail{width:120px;height:120px;border-radius:50%;background:var(--green);display:flex;flex-direction:column;align-items:center;justify-content:center;color:#fff;font-weight:700;font-size:14px;line-height:1.4;text-align:center}
.schedule{margin-top:30px;width:100%;border-collapse:collapse}
.schedule th,.schedule td{border:1px solid var(--line);padding:6px 10px;text-align:left}
.schedule th{background:var(--panel);width:180px}
.site-footer{position:absolute;left:0;right:0;top:3200px;height:56px;background:var(--green-dark);color:#fff;text-align:center;line-height:56px;font-size:12px}
</style>
</head>
<body>
<header class="site-header">
  <div class="brand"><span class="brand-mark"></span>森金堂</div>
  <div class="brand-sub">日本の器と雑貨 陶器 の店</div>
  <div class="search"><div class="search-field"></div><div class="search-btn">検索</div></div>
  <div class="tel">03-5550-0182</div>
</header>
<nav class="global-nav">
  <a>森金堂トップ</a><a>マイページ</a><a>お客様の声</a><a>ご利用ガイド</a><a>よくあるご質問</a><a>お問い合わせ</a>
</nav>

<div class="layout">
  <aside class="sidebar">
    <div class="side-block"><div class="side-title">商品検索</div><div class="search-field" style="width:100%"></div></div>
    <div class="side-block">
      <div class="side-title">商品種類</div>
      <ul class="side-list"><li>珪藻土コースター</li><li>無地（1枚）</li><li>絵柄付き（1枚）</li><li>コースターセット</li><li>オリジナルコースター</li></ul>
    </div>
    <div class="side-block">
      <div class="side-title">商品種類別</div>
      <ul class="side-list"><li>珪藻土コースター</li><li>珪藻土アロマプレート</li><li>珪藻土バスマット</li><li>ゆかいな雑貨＆小物</li><li>その他</li><li>お得なセット</li></ul>
    </div>
    <div class="side-block">
      <div class="side-title">価格</div>
      <ul class="side-list"><li>6,000円〜</li><li>〜6,000円</li><li>〜3,000円</li><li>〜1,000円</li></ul>
    </div>
    <div class="side-banner">お電話・FAX<small>でもご注文いただけます。お気軽にどうぞ。</small></div>
    <div class="side-point">100分<small>のポイントプレゼント</small></div>
    <div class="side-affiliate">アフィリエイターさん募集。10%</div>
    <div class="side-block">
      <div class="side-title">注目キーワード</div>
      <p style="padding:4px 8px">珪藻土コースター 珪藻土プレート 珪藻土バスマット</p>
    </div>
    <div class="side-block">
      <div class="side-title">カレンダー</div>
      <table class="calendar">
        <tr><td class="closed">日</td><td>月</td><td>火</td><td>水</td><td>木</td><td>金</td><td class="closed">土</td></tr>
        <tr><td class="closed">1</td><td>2</td><td>3</td><td>4</td><td>5</td><td>6</td><td class="closed">7</td></tr>
        <tr><td class="closed">8</td><td>9</td><td>10</td><td>11</td><td>12</td><td>13</td><td class="closed">14</td></tr>
        <tr><td class="closed">15</td><td>16</td><td>17</td><td>18</td><td>19</td><td>20</td><td class="closed">21</td></tr>
        <tr><td class="closed">22</td><td>23</td><td>24</td><td>25</td><td>26</td><td>27</td><td class="closed">28</td></tr>
      </table>
      <p style="padding:6px 2px">赤色は休業日です。休業日のご注文は翌営業日の対応となります。</p>
    </div>
    <div class="side-block">
      <div class="side-title">関連サイトリンク</div>
      <div class="partner"></div>
      <div class="partner"></div>
      <p>森金堂陶器株式会社</p>
    </div>
  </aside>

  <main class="main">
    <div class="breadcrumb">HOME ＞ 珪藻土コースター</div>
    <section class="offers">
      <div class="offer">
        <div><p>毎月、いろいろな絵柄の<em>「珪藻土コースター」</em>を少しずつ増やしてそろえたい方に！</p><span class="offer-btn">一般のお客さま</span></div>
        <div class="offer-photo" role="img" aria-label="絵柄付き珪藻土コースターの写真"></div>
      </div>
      <div class="offer">
        <div><p><em>「珪藻土コースター」</em>をお使いの飲食店様の吸水性維持に、毎月交換用に！</p><span class="offer-btn">飲食店さま</span></div>
        <div class="offer-photo" role="img" aria-label="店舗スタッフの写真"></div>
      </div>
    </section>
    <p class="order-note">1枚からご注文いただけます！</p>

    <section class="hero">
      <div class="hero-tag">とっても お得な</div>
      <div class="hero-course">毎月お届けコース</div>
      <div class="hero-photo" role="img" aria-label="グラスと珪藻土コースターの写真"></div>
      <div class="hero-brand">森金堂</div>
      <h1 class="hero-title"><small>給水実力 コースター</small>オリジナル<br>「珪藻土コースター」<small>●枚セット</small></h1>
      <div class="hero-badges"><span>驚きの<br>吸水力</span><span>天然<br>素材</span><span>速乾<br>性</span><span>高品質</span></div>
      <div class="hero-price">0,000<small>円 送料無料</small></div>
    </section>

    <section class="feature">
      <div class="feature-head">吸水力<small>は</small>業界随一</div>
      <div class="feature-lead">品質には絶対の自信があります</div>
      <div class="feature-photo" role="img" aria-label="コースターが水を吸う様子の写真"></div>
    </section>
    <section class="feature second">
      <div class="feature-head">コースター<small>なのに</small>陶器</div>
      <div class="feature-lead">見た目の高級感も満足いただけます</div>
      <div class="feature-photo" role="img" aria-label="グラスを置いた陶器コースターの写真"></div>
    </section>

    <h2 class="about-head"><span>給水実力コースター</span>オリジナル「珪藻土コースター」毎月お届けコースとは？</h2>
    <p class="about-lead">毎月、1枚から<b>「珪藻土コースター」</b>を<b>定期的</b>にお届けいたします。<br>（もちろん、まとめてお届けも可能です）<br>いつも<b>お得</b>にお取り扱いいただける当店のオリジナルのサービスです。</p>
    <div class="about-body">
      <div class="about-text">
        <p>珪藻土コースターは、その吸水性と高級感から飲食店さまにも多くご導入いただいております。ただし、長くお使いいただくと表面の目詰まりから吸水性が少しずつ落ちてまいります。</p>
        <p>そこで、吸水力が落ちたコースターを少しずつ新品と交換していただけるよう、毎月定期的にお届けするプランをご用意いたしました。常に高い吸水力の状態でお使いいただけます。</p>
      </div>
      <div class="about-img" role="img" aria-label="無地の珪藻土コースターの写真"></div>
      <div class="about-img pattern" role="img" aria-label="絵柄付きコースターの写真"></div>
    </div>
    <div class="summary">
      定期的に数枚ずつご購入いただき、吸水性が落ちたものと交換していただくことで、<b>いつも吸水力の高い状態</b>を維持できます。<br>
      この定期購入プランでは、<b>最低継続購入期間3ヶ月</b>とさせていただきますが、<b>通常より安価</b>でご購入いただけます。
    </div>

    <section class="product">
      <h2>「珪藻土コースター●●」毎月、定期的にお届けします。</h2>
      <p>商品名：「珪藻土コースター●●毎月お届けコース●枚セット」</p>
    </section>

    <section class="details">
      <div class="icons">
        <div class="icon-day"><small>毎月</small>15日<small>発送</small></div>
        <div class="icon-mail">
          <svg width="54" height="38" viewBox="0 0 54 38" aria-hidden="true"><rect x="1" y="1" width="52" height="36" fill="none" stroke="#fff" stroke-width="3"/><path d="M2 2 27 22 52 2" fill="none" stroke="#fff" stroke-width="3"/></svg>
          メール便<br>で発送
        </div>
      </div>
      <h3>【お届け内容】</h3>
      <p>・お届け方法：メール便</p>
      <p>・お届け枚数：毎月●枚</p>
      <p>・お支払方法：クレジットカード決済のみ</p>
      <p>・最低継続期間：3ヶ月（3回）</p>
      <p>・価格：●●●円（税込・送料無料）</p>
      <h3>【お支払いについて】</h3>
      <p>・お申込み後、毎月の発送前にご登録のカードで決済いたします。</p>
      <p>・継続期間終了後は自動で更新されます。解約はお問い合わせからご連絡ください。</p>
      <p>・ご入金後の返品・交換は、商品の不良の場合のみ承ります。</p>
      <h3>【商品の発送とお支払いのスケジュールについて】</h3>
      <p>・お届けは毎月15日発送となります。月末締め、翌月15日にお届けの商品を発送いたします。</p>
      <table class="schedule">
        <tr><th>月末</th><td>翌月分のお申込み締め切り</td></tr>
        <tr><th>毎月1日〜10日</th><td>ご登録のカードで決済</td></tr>
        <tr><th>毎月15日</th><td>メール便にて商品を発送</td></tr>
        <tr><th>発送後2〜4日</th><td>お客様のお手元にお届け</td></tr>
      </table>
      <p style="margin-top:20px">※ 休業日の関係で発送日が前後する場合がございます。あらかじめご了承ください。</p>
    </section>
  </main>
</div>
<footer class="site-footer">Copyright © 森金堂陶器株式会社 All Rights Reserved.</footer>
</body>
</html>
```